Quillfern Nightclub Flyer (Updated)

Flyer for facebook, square is fine, or rectangular. Here is the text:
QUILLFERN
Nightclub + Lounge
presents

SPLIT DECK WEDNESDAY
Nov 29 2018

CLUB FLOOR:
GORDY B2B RALPH
THEODORE BRUSKVIK

LOUNGE:
OTIS B2B HALF TIDE
COPPER FENWICK

Powered by HALVERN Acoustics
4716 Larchmere Avenue 21+ 9pm-2am
quillfernvenue-example.com for VIP booth inquiries

Target Market(s)

Nightclub

Industry/Entity Type

Night Club

Font styles to use
Sans Serif

Colors

Designer to choose colors to be used in the design.

Requirements
Must have
• All the text listed, and plz keep the theme of the attached files. We want to stay consistent with the Quillfern brand
Nice to have
• Try to stay with the theme from the attachments
Should not have
• Dont' stray to far from the general theme we have from the attachments

```html
<!DOCTYPE html>
<html lang="en">
<head>
<meta charset="utf-8">
<title>Quillfern Nightclub – Split Deck Wednesday</title>
<link rel="stylesheet" href="https://fonts.googleapis.com/css2?family=Open+Sans:wght@400;600;700&display=swap">
<style>
  :root {
    --page: #e4e6ea;
    --ink: #231f20;
    --gold: #c8995b;
    --gold-deep: #8a6a3c;
    --olive: #c9d08a;
    --white: #ffffff;
  }
  * { margin: 0; padding: 0; box-sizing: border-box; }
  html, body {
    width: 1200px; height: 1200px; overflow: hidden;
    background: var(--page);
    font-family: "Open Sans", Arial, sans-serif;
  }
  .flyer {
    position: absolute; left: 30px; top: 302px;
    width: 1140px; height: 596px;
    background: var(--ink);
    overflow: hidden;
    color: var(--white);
  }
  .ornament {
    position: absolute; left: 0; top: 242px;
    width: 290px; height: 354px;
  }
  .brand {
    position: absolute; left: 0; right: 0; top: 22px;
    display: flex; justify-content: center; align-items: center;
    gap: 16px; padding-left: 150px;
  }
  .brand-dot {
    width: 86px; height: 86px; border-radius: 50%;
    background: var(--olive);
  }
  .brand-words { display: flex; flex-direction: column; }
  .brand-name {
    font-size: 60px; font-weight: 400; line-height: 1;
    color: var(--olive); letter-spacing: 1px;
  }
  .brand-tag {
    margin-top: 6px;
    font-size: 14px; font-weight: 400; letter-spacing: 5px;
    color: var(--olive);
  }
  .presents {
    position: absolute; left: 0; right: 0; top: 117px;
    text-align: center; padding-left: 80px;
    font-size: 26px; font-weight: 700; letter-spacing: 1px;
  }
  .headline {
    position: absolute; left: 0; right: 0; top: 190px;
    text-align: center; padding-left: 150px;
    font-size: 44px; font-weight: 700; letter-spacing: 1.5px;
    line-height: 1; white-space: nowrap;
  }
  .headline-event { color: var(--gold); }
  .headline-date { color: var(--white); }
  .stage {
    position: absolute; top: 283px;
    width: 272px; height: 180px;
    border: 4px solid var(--gold);
    padding: 62px 0 0 26px;
    font-size: 18px; font-weight: 400; line-height: 22px;
    text-transform: uppercase; white-space: nowrap;
  }
  .stage-club { left: 311px; }
  .stage-lounge { left: 696px; }
  .details {
    position: absolute; left: 701px; top: 502px;
    font-size: 16.5px; font-weight: 600; line-height: 23px;
    white-space: nowrap;
  }
</style>
</head>
<body>
  <main class="flyer">
    <svg class="ornament" role="img" aria-label="Gold mandala ornament rising from the left edge" viewBox="0 0 290 354">
      <defs>
        <radialGradient id="mandala-tone" cx="0" cy="0.5" r="1">
          <stop offset="0" stop-color="#c8995b"/>
          <stop offset="1" stop-color="#8a6a3c"/>
        </radialGradient>
      </defs>
      <circle cx="0" cy="200" r="250" fill="url(#mandala-tone)"/>
    </svg>

    <header class="brand">
      <span class="brand-dot"></span>
      <div class="brand-words">
        <span class="brand-name">QUILLFERN</span>
        <span class="brand-tag">NIGHTCLUB + LOUNGE</span>
      </div>
    </header>

    <p class="presents">PRESENTS</p>

    <h1 class="headline">
      <span class="headline-event">SPLIT DECK WEDNESDAY</span>
      <span class="headline-date">NOV 29 2018</span>
    </h1>

    <section class="stage stage-club">
      <p>Club Floor:</p>
      <p>Gordy B2B Ralph</p>
      <p>Theodore Bruskvik</p>
    </section>

    <section class="stage stage-lounge">
      <p>Lounge:</p>
      <p>Otis B2B Half Tide</p>
      <p>Copper Fenwick</p>
    </section>

    <footer class="details">
      <p>Powered by HALVERN Acoustics</p>
      <p>4716 Larchmere Avenue 21+ 9pm-2am</p>
      <p>quillfernvenue-example.com for VIP booth inquiries</p>
    </footer>
  </main>
</body>
</html>
```